Bright and beautiful business card for a coach

I'm a personal and business coach based in Perth, Australia. I need a business card that whilst subtle and elegant, will stand out and appeal on a table full of cards.

My business name is Tide Mentoring and the business card must represent the warmth and brightness implied in the name, without being gimmicky. It must have a warmth and appeal and be easy to read.

I prefer clean, minimalist designs.

It must align with the feel of my website and socials: https://www.tidementoring.com.au/
https://www.instagram.com/tidementoringau/
https://www.facebook.com/tidementoringau
Updates

Hi Designers Thank you so much for taking the time to submit designs. I wonder if I could have explained myself a little better. Most of the designs that have been submitted look rather formal and many have quite corporate looking embellishments on them (to my eye). I would like softer, warmer, more organic. I’m open to people playing about and being more abstract, using softer embellishments (e.g the line drawing flowers and grasses I’ve used in my socials) incorporating other colours from my palette or like the social icons in my email signature (in PDF), perhaps playing with size/oversize, playing with the bleed. Please don’t be constrained by what I’ve already done, it merely needs to compliment. I’m sorry if I’m not using the right words or have led you astray. I’m no designer, but I’ve done my website, socials, email signature etc all myself (my logo was a design contest) and I was really hoping for my business card to be something more creative than I could have made with a template. Reminder: No black cards/sides please. Thank you 😊

Target Market(s)

Individuals, most likely but not all female. Creative thinkers. Likely professionals.

Industry/Entity Type

Business & Personal Coach

Contact Information for Business Card

(Tide Mentoring Logo) Name: Maren Delsby; Title: Business & Personal Coach; Phone number: +61 (0)438 915307; Email: maren@tidementoring.com.au; Website: https://tidementoring.com.au; Social icons for Facebook, Instagram & LinkedIn: @tidementoringAU. Optional strapline: "A thinking partner to help you cut through the noise"

Font styles to use
Sans Serif

Colors
00AB8E
00BBA5
67D7C9
C6EFE9
E9F9F6
59FF00
82FF00
B8FF75
E3FFCB
F4FFEA
FFC000
F8CF3A
FAE287
FDF2CF
FEFAEE

Requirements
Must have
• Must align with feel of my website and socials. Must have a pop of #FFC000 (possibly whole of one side, or at least a block). Bright or white background. Easy to read.
Nice to have
• Possibly incorporate the sunshine/grass picture I have used in website and socials - will upload.
Should not have
• Must not be black or dark. Not impersonal or corporate looking.

```html
<!DOCTYPE html>
<html lang="en">
<head>
<meta charset="utf-8">
<title>Tide Mentoring – Business Card</title>
<link rel="stylesheet" href="https://fonts.googleapis.com/css2?family=Allura&family=Dawning+of+a+New+Day&family=Lato:wght@300;400&display=swap">
<style>
  :root {
    --page-bg: #b3b3b3;
    --card-white: #ffffff;
    --gold-top: #f6c51c;
    --gold-mid: #e2a10c;
    --gold-bottom: #c06a1a;
    --gold-text: #d9930f;
    --gold-line: #f0b93a;
    --ray-gold: #e9a820;
    --text-grey: #6f6f6f;
    --soft-grey: #9a9a9a;
  }
  * { box-sizing: border-box; margin: 0; padding: 0; }
  html, body { width: 1200px; height: 900px; overflow: hidden; }
  body {
    background: var(--page-bg);
    font-family: "Lato", Arial, sans-serif;
    position: relative;
  }
  .card {
    position: absolute;
    top: 90px;
    width: 440px;
    height: 720px;
    overflow: hidden;
  }
  /* Front side */
  .card--front {
    left: 130px;
    background: linear-gradient(180deg, var(--gold-top) 0%, var(--gold-mid) 38%, var(--gold-bottom) 100%);
  }
  .brand-disc {
    position: absolute;
    left: 50%;
    top: 290px;
    width: 240px;
    height: 240px;
    margin: -120px 0 0 -120px;
    border-radius: 50%;
    background: var(--card-white);
    display: flex;
    align-items: center;
    justify-content: center;
  }
  .brand-name {
    font-family: "Lato", Arial, sans-serif;
    font-weight: 400;
    font-size: 22px;
    letter-spacing: 0.32em;
    line-height: 1.6;
    text-align: center;
    color: var(--gold-text);
    text-transform: uppercase;
    padding-left: 0.32em;
  }
  /* Back side */
  .card--back {
    left: 630px;
    background: var(--card-white);
  }
  .sun-rays {
    position: absolute;
    left: -150px;
    top: 250px;
    width: 340px;
    height: 360px;
    border-radius: 50%;
    background: radial-gradient(circle at 30% 55%, rgba(233,168,32,0) 0%, rgba(233,168,32,0) 34%, rgba(233,168,32,0.55) 46%, rgba(233,168,32,0.25) 66%, rgba(233,168,32,0) 72%);
  }
  .contact {
    position: absolute;
    top: 48px;
    right: 36px;
    width: 300px;
    text-align: left;
  }
  .contact__name {
    font-family: "Allura", cursive;
    font-size: 52px;
    color: var(--gold-text);
    line-height: 1;
    text-align: right;
    padding-right: 6px;
  }
  .contact__title {
    font-size: 14px;
    color: var(--text-grey);
    letter-spacing: 0.04em;
    margin-top: 6px;
    padding-bottom: 8px;
    border-bottom: 1.5px solid var(--gold-line);
  }
  .contact__list { list-style: none; margin-top: 8px; }
  .contact__item {
    display: flex;
    align-items: center;
    gap: 8px;
    font-size: 14px;
    color: var(--text-grey);
    line-height: 1.6;
  }
  .contact__icon { width: 12px; height: 12px; flex: none; }
  .strapline {
    position: absolute;
    top: 300px;
    left: 170px;
    width: 240px;
    font-family: "Dawning of a New Day", cursive;
    font-size: 34px;
    line-height: 1.25;
    color: var(--soft-grey);
    text-align: center;
  }
  .strapline__lead { font-size: 48px; display: block; }
  .social-handle {
    position: absolute;
    bottom: 40px;
    left: 0;
    right: 0;
    text-align: center;
    font-size: 16px;
    color: var(--text-grey);
    letter-spacing: 0.02em;
  }
</style>
</head>
<body>
  <section class="card card--front" aria-label="Business card front">
    <div class="brand-disc">
      <p class="brand-name">Tide<br>Mentoring</p>
    </div>
  </section>

  <section class="card card--back" aria-label="Business card back">
    <div class="sun-rays" role="img" aria-label="Golden sunburst rays rising from the left edge"></div>

    <div class="contact">
      <h1 class="contact__name">Maren Delsby</h1>
      <p class="contact__title">Business &amp; Personal Coach</p>
      <ul class="contact__list">
        <li class="contact__item">
          <svg class="contact__icon" viewBox="0 0 12 12" aria-hidden="true"><path d="M2.5 1 L4.5 1 L5.2 3.4 L4 4.4 C4.6 5.8 6.2 7.4 7.6 8 L8.6 6.8 L11 7.5 L11 9.5 C11 10.3 10.3 11 9.5 11 C5 11 1 7 1 2.5 C1 1.7 1.7 1 2.5 1 Z" fill="#d9930f"/></svg>
          +61 (0)438 915307
        </li>
        <li class="contact__item">
          <svg class="contact__icon" viewBox="0 0 12 12" aria-hidden="true"><rect x="1" y="2.5" width="10" height="7" rx="1" fill="#d9930f"/><path d="M1.5 3 L6 6.5 L10.5 3" stroke="#fff" stroke-width="1" fill="none"/></svg>
          maren@tidementoring.com.au
        </li>
        <li class="contact__item">
          <svg class="contact__icon" viewBox="0 0 12 12" aria-hidden="true"><circle cx="6" cy="6" r="5" fill="none" stroke="#d9930f" stroke-width="1.2"/><ellipse cx="6" cy="6" rx="2.2" ry="5" fill="none" stroke="#d9930f" stroke-width="1"/><path d="M1 6 H11" stroke="#d9930f" stroke-width="1"/></svg>
          www.tidementoring.com.au
        </li>
      </ul>
    </div>

    <p class="strapline">
      <span class="strapline__lead">A</span>
      thinking partner<br>to<br>help you<br>cut through<br>the noise
    </p>

    <p class="social-handle">@tidementoringAU.</p>
  </section>
</body>
</html>
```